Osmer wine Label, 750ml bottle

We need a wine label that is simple, clean, and timeless. The final project should reflect a premium product. All ideas encouraged. A label that is eye catching and gives of a pristine look. The wine is a Red Blend of Zinfandel, Syrah, Grenache, and Tempranillo. All Californian fruit and hand crafted. The wine is really something special and the label should reflect that. The label must also be able to carry many tiers, the addition of some other labels based around this label may take place in the future.

Target Market(s)

All ideas welcome

Industry/Entity Type

Retail

Font styles to use
Serif

Requirements
Must have
• Open to all ideas.
Nice to have
• An elegant look, simple colors, however, some sort of eye catching effect.
Should not have
• Should not be quirky.

```html
<!DOCTYPE html>
<html lang="en">
<head>
<meta charset="utf-8">
<title>Red Blend Label – 750 ml</title>
<link href="https://fonts.googleapis.com/css2?family=Playfair+Display:wght@400;500&family=Tinos:ital@0;1&display=swap" rel="stylesheet">
<style>
  :root {
    --backdrop: #ece7df;
    --paper: #ffffff;
    --gold: #d8b44c;
    --gold-soft: #e4c977;
    --ornament: #b46a2a;
    --ink: #111111;
  }
  * { margin: 0; padding: 0; box-sizing: border-box; }
  html, body {
    width: 1200px;
    height: 1200px;
    overflow: hidden;
    background: var(--backdrop);
  }
  .canvas {
    position: relative;
    width: 1200px;
    height: 1200px;
  }
  .label {
    position: absolute;
    left: 220px;
    top: 88px;
    width: 760px;
    height: 1024px;
    background: var(--paper);
    box-shadow: 0 6px 24px rgba(0,0,0,0.12);
  }
  .band-top {
    position: absolute;
    left: 0; right: 0; top: 0;
    height: 20px;
    background: var(--gold);
  }
  .band-bottom {
    position: absolute;
    left: 0; right: 0; bottom: 0;
    height: 44px;
    background: var(--gold);
  }
  .frame-outer {
    position: absolute;
    left: 20px; right: 20px;
    top: 52px; bottom: 72px;
    border: 3px solid var(--gold-soft);
  }
  .frame-inner {
    position: absolute;
    inset: 8px;
    border: 2px solid var(--gold-soft);
  }
  .content {
    position: absolute;
    inset: 0;
    text-align: center;
    color: var(--ink);
    font-family: "Tinos", "Times New Roman", serif;
  }
  .vintage {
    position: absolute;
    left: 0; right: 0; top: 86px;
    font-style: italic;
    font-size: 38px;
  }
  .crest {
    position: absolute;
    left: 90px;
    top: 170px;
    width: 580px;
    height: 276px;
  }
  .wordmark {
    position: absolute;
    left: 0; right: 0; top: 440px;
    font-family: "Playfair Display", "Bodoni Moda", serif;
    font-weight: 400;
    font-size: 172px;
    line-height: 1;
    letter-spacing: -2px;
  }
  .tagline {
    position: absolute;
    left: 0; right: 0; top: 640px;
    font-size: 28px;
  }
  .blend-intro {
    position: absolute;
    left: 0; right: 0; top: 760px;
    font-size: 24px;
  }
  .varieties {
    position: absolute;
    left: 0; right: 0; top: 796px;
    font-size: 31px;
  }
  .volume-row {
    position: absolute;
    left: 0; right: 0; top: 878px;
    display: flex;
    justify-content: center;
    align-items: center;
    gap: 26px;
  }
  .volume {
    font-size: 36px;
  }
  .flourish {
    width: 200px;
    height: 44px;
  }
</style>
</head>
<body>
  <div class="canvas">
    <div class="label">
      <div class="band-top"></div>
      <div class="frame-outer"><div class="frame-inner"></div></div>
      <div class="band-bottom"></div>

      <div class="content">
        <p class="vintage">2016</p>

        <svg class="crest" viewBox="0 0 580 276" role="img" aria-label="Ornate copper scrollwork crest framing a monogram">
          <defs>
            <radialGradient id="crestTone" cx="50%" cy="50%" r="60%">
              <stop offset="0%" stop-color="#c98a4b" stop-opacity="0.55"/>
              <stop offset="100%" stop-color="#c98a4b" stop-opacity="0.12"/>
            </radialGradient>
          </defs>
          <rect x="0" y="0" width="580" height="276" rx="20" fill="url(#crestTone)"/>
        </svg>

        <h1 class="wordmark">Wine</h1>
        <p class="tagline">All Californian Fruit and Hand Crafted</p>

        <p class="blend-intro">Red blend of</p>
        <p class="varieties">Zinfandel, Syrah, Grenache, and Tempranillo</p>

        <div class="volume-row">
          <svg class="flourish" viewBox="0 0 200 44" role="img" aria-label="Copper scroll flourish">
            <rect x="0" y="8" width="200" height="28" rx="14" fill="#c98a4b" fill-opacity="0.35"/>
          </svg>
          <span class="volume">750 ml</span>
          <svg class="flourish" viewBox="0 0 200 44" role="img" aria-label="Copper scroll flourish">
            <rect x="0" y="8" width="200" height="28" rx="14" fill="#c98a4b" fill-opacity="0.35"/>
          </svg>
        </div>
      </div>
    </div>
  </div>
</body>
</html>
```